someone who can choose good colours and fonts and a style for an already layed out web page

HI

We need someone who can choose good colors and fonts and style for an already layed out web page.

please look at the first file.

The hard part of what needs to go where is already done,

1) we just need a type of character suitable for our business

2) colors probably in the green / yellow spectrum to suit our business

3) we need you to choose the style. For example you could choose round photos, or square buttons, video boxes with or without frames, that sort of stuff, just tweaking of what is there. plain arial is probably what we'd like but with text but with script or memorable headings. We would just like a design style that you think would be good gor our business model.

4) the twitter,facebook logo needs to be put in a new place

our project is an Italian style village in Italy called "Casale Delle Rondini", in Abruzzo, Italy.
It is surrounded by vineyards, lake and olive trees.

The most important is that it looks expensive, the village is eco friendly so anything on those lines is great, Obviously Italian, so italian looking characters

our website is www.collinetorre.com but we are updating it. we like the style of the old site , but it is too out of date

you can create the layout using the files we've given below and boxes
Updates

hi we've just updated out brief to make it more simple, its actually not much work its just about design choices

Target Market(s)

all lovers of Italian things
eco frienly

Industry/Entity Type

Business

Font styles to use
Decorative
Script

Colors
fcf9ce
faee3f
fde18a
fece3e
cadf82
9bcb3b
acd036
fce7d2
ec2027

Requirements
Must have
• has to have the same layout or similar so as all the boxes and links are in there
twitter,facebook and other logos need to be present where you want them
Nice to have
• we have chosen some colors but you can choose others 3 or 4 are usual a good number with a light yellow background maybe....
Should not have
• no old style must look up to date

```html
<!DOCTYPE html>
<html lang="en">
<head>
<meta charset="utf-8">
<title>Casale Delle Rondini</title>
<link rel="stylesheet" href="https://fonts.googleapis.com/css2?family=Pinyon+Script&family=Arimo:wght@400&display=swap">
<style>
  :root {
    --red: #e41e26;
    --red-deep: #b8141b;
    --maroon: #3f0c0e;
    --maroon-dark: #120202;
    --green: #9bcb3b;
    --green-deep: #5f8a24;
    --cream: #fbe6d4;
    --white: #ffffff;
    --ink: #2a0606;
    --script: "Pinyon Script", cursive;
    --sans: "Arimo", Arial, sans-serif;
  }
  * { box-sizing: border-box; margin: 0; padding: 0; }
  html, body { width: 900px; height: 1200px; overflow: hidden; background: var(--cream); }
  .page { position: relative; width: 900px; height: 1200px; overflow: hidden; font-family: var(--sans); }

  .topbar { position: absolute; left: 0; top: 0; width: 900px; height: 132px;
    background: linear-gradient(180deg, var(--red-deep), var(--red) 60%, #d81a22); }
  .contact { position: absolute; right: 22px; top: 28px; color: var(--white); font-size: 24px; line-height: 40px; letter-spacing: 0.5px; text-align: left; }

  .hero { position: absolute; left: 0; top: 130px; width: 900px; height: 322px;
    background: linear-gradient(90deg, #9bcb3b 0%, #9fce3e 60%, #7da82f 90%, #6b9528 100%); }

  .brand-oval { position: absolute; left: -42px; top: 2px; width: 512px; height: 462px; border-radius: 50%;
    background: var(--white); border: 9px solid var(--red); box-shadow: 0 4px 10px rgba(0,0,0,.35); }
  .brand-name { position: absolute; left: 10px; top: 325px; font-family: var(--script); font-size: 50px; color: var(--red); white-space: nowrap; }

  .slideshow { position: absolute; left: 495px; top: 153px; width: 405px; height: 265px;
    background: linear-gradient(90deg, var(--maroon-dark), #2a0808 60%, #4a0f0f);
    display: flex; align-items: center; justify-content: center; text-align: center;
    font-family: var(--script); font-size: 66px; line-height: 70px; color: var(--white); }

  .nav { position: absolute; left: 0; top: 452px; width: 900px; height: 74px; background: var(--maroon); display: flex; }
  .nav a { display: flex; align-items: center; justify-content: center; font-family: var(--script); font-size: 30px; color: var(--white); text-decoration: none; border-right: 4px solid var(--red); }
  .nav a:last-child { border-right: none; }

  .content { position: absolute; left: 0; top: 526px; width: 900px; height: 414px; background: var(--cream); }
  .content h1 { position: absolute; left: 22px; top: 52px; font-family: var(--script); font-weight: 400; font-size: 58px; color: var(--maroon); white-space: nowrap; }
  .content p { position: absolute; left: 22px; top: 136px; width: 552px; font-size: 14.6px; line-height: 16.2px; color: var(--ink); }

  .site-plan { position: absolute; left: 580px; top: 49px; width: 286px; height: 233px; border: 3px solid var(--red-deep);
    background: radial-gradient(circle at 40% 50%, #7fc04a, #b8d97a 45%, #f6f1d8 80%);
    box-shadow: 6px 6px 10px rgba(0,0,0,.45); }
  .seasonal { position: absolute; left: 580px; top: 292px; width: 286px; text-align: center; font-size: 40px; line-height: 40px; color: var(--maroon); }

  .divider { position: absolute; left: 0; top: 940px; width: 900px; height: 12px; background: var(--red); }
  .newsletter { position: absolute; left: 0; top: 952px; width: 226px; height: 160px; background: var(--maroon);
    display: flex; align-items: center; justify-content: center; text-align: center; color: var(--white); font-size: 31px; line-height: 35px; }
  .booking { position: absolute; left: 226px; top: 952px; width: 674px; height: 160px;
    background: radial-gradient(ellipse at 30% 50%, #87b43a, #6d9a2c 55%, #3f5f1c 100%);
    display: flex; align-items: center; justify-content: center; font-family: var(--script); font-size: 84px; color: var(--white); text-shadow: 3px 4px 5px rgba(0,0,0,.5); }

  .footer { position: absolute; left: 0; top: 1112px; width: 900px; height: 88px; background: linear-gradient(180deg, var(--red), var(--red-deep)); }
  .blog { position: absolute; left: 40px; top: 8px; font-family: var(--script); font-size: 62px; color: var(--white); }
  .follow { position: absolute; left: 432px; top: 14px; font-family: var(--script); font-size: 48px; color: var(--white); }
  .social { position: absolute; left: 710px; top: 32px; display: flex; gap: 26px; }
  .social span { width: 28px; height: 28px; border-radius: 50%; background: var(--white); display: block; }
</style>
</head>
<body>
<div class="page">
  <header class="topbar">
    <div class="contact">Telephone: 0851234567<br>Via dei Mandorli 12, Colle Alto</div>
  </header>

  <section class="hero">
    <div class="brand-oval"></div>
    <div class="brand-name">Casale Delle Rondini</div>
  </section>
  <div class="slideshow">Revolving<br>Photos</div>

  <nav class="nav">
    <a href="#" style="width:228px">Description</a>
    <a href="#" style="width:239px">Which Reason</a>
    <a href="#" style="width:240px">Price List</a>
    <a href="#" style="width:193px">Examples</a>
  </nav>

  <main class="content">
    <h1>Casale Delle Rondini</h1>
    <p>Casale Delle Rondini is built in traditional Italian architectural style and surrounded by olive groves, vineyards,a beautiful lake surrounded by a park with wildlife. The panoramic view of the mountains is breathtaking and you can see for 30 miles on a clear day. Red and white umbrellas, barbeques, swimming pools and a spa will contribute to its unique atmosphere. there will also be a health farm, where you can treat yourself to a luxurious massage. Ten shops and ensure any of your other needs can be met. Casale Delle Rondini is ensconced in the beauty of the Italian countryside, where the hot white sandy beaches of the Adriatic coastline meet the cold snowy ski-slopes of the Appenine mountains, with Rome only a short car ride away. Each property will be in the OLD Abruzzo style, with attractive brick and stone walls. There are one-, two- and three-bedroomed apartments and three- or four-bedroomed villas.</p>
    <div class="site-plan" role="img" aria-label="Illustrated site plan of the village phases with gardens, lake and playground"></div>
    <div class="seasonal">Seasonal<br>Photos</div>
  </main>

  <div class="divider"></div>
  <div class="newsletter">Sign up<br>for our<br>newsletter!</div>
  <div class="booking">Book your trip!</div>

  <footer class="footer">
    <div class="blog">Blog</div>
    <div class="follow">Follow Us:</div>
    <div class="social" aria-label="Social links"><span></span><span></span><span></span></div>
  </footer>
</div>
</body>
</html>
```